Directing people to check over 2000 new Portugal listings on the site

A copy of our failed attempt is annexed. graphics should be 197x650px and 448x81px

Target Market(s)

Global property Buyers

Requirements
Nice to have
• Euro map with portugal isolated

```html
<!DOCTYPE html>
<html lang="en">
<head>
<meta charset="utf-8">
<title>New Portugal Listings Banners</title>
<link rel="stylesheet" href="https://fonts.googleapis.com/css2?family=Montserrat:wght@800&display=swap">
<style>
  :root {
    --page: #ffffff;
    --ink: #000000;
    --white: #ffffff;
    --green: #6a9a31;
    --map-light: #eef0e8;
    --map-mid: #e3e6dc;
    --cursor: #e8201d;
  }
  html, body {
    margin: 0;
    width: 1200px;
    height: 1188px;
    overflow: hidden;
    background: var(--page);
    font-family: "Montserrat", "Futura", sans-serif;
    font-weight: 800;
  }
  .banner {
    position: absolute;
    background: var(--ink);
    border: 2px solid var(--ink);
    box-sizing: border-box;
    overflow: hidden;
    color: var(--white);
    text-transform: uppercase;
    text-align: center;
  }
  .map-area {
    position: absolute;
    background: linear-gradient(160deg, var(--map-light), var(--map-mid));
  }
  .cursor { position: absolute; }
  .headline-box {
    position: absolute;
    background: var(--green);
    display: flex;
    align-items: center;
    justify-content: center;
    line-height: 1;
    text-shadow: 2px 3px 2px rgba(0,0,0,.85);
    letter-spacing: .04em;
    box-sizing: border-box;
  }
  .subline {
    position: absolute;
    margin: 0;
    left: 0; right: 0;
    letter-spacing: .02em;
  }
  .cta {
    position: absolute;
    background: var(--green);
    border-radius: 6px;
    display: flex;
    align-items: center;
    justify-content: center;
    text-shadow: 1px 2px 1px rgba(0,0,0,.85);
    letter-spacing: .1em;
  }

  /* Skyscraper 197x650 */
  .banner--tall { left: 101px; top: 120px; width: 288px; height: 951px; }
  .banner--tall .map-area {
    left: 0; top: 0; width: 100%; height: 365px;
    -webkit-mask: linear-gradient(#000 76%, transparent);
            mask: linear-gradient(#000 76%, transparent);
  }
  .banner--tall .cursor { left: 108px; top: 200px; width: 56px; height: 92px; }
  .banner--tall .headline-box {
    left: 20px; top: 400px; width: 249px; height: 170px;
    flex-direction: column; font-size: 56px; gap: 14px;
  }
  .banner--tall .subline { top: 612px; font-size: 41px; line-height: 60px; }
  .banner--tall .cta { left: 25px; top: 834px; width: 237px; height: 56px; font-size: 19px; }

  /* Leaderboard 448x81 */
  .banner--wide { left: 445px; top: 120px; width: 653px; height: 117px; }
  .banner--wide .map-area {
    left: 0; top: 0; width: 200px; height: 100%;
    -webkit-mask: linear-gradient(90deg, #000 60%, transparent);
            mask: linear-gradient(90deg, #000 60%, transparent);
  }
  .banner--wide .cursor { left: 87px; top: 46px; width: 28px; height: 48px; }
  .banner--wide .headline-box { left: 309px; top: 14px; width: 210px; height: 47px; font-size: 25px; }
  .banner--wide .subline { left: 200px; width: 451px; top: 76px; font-size: 21px; line-height: 1; }
</style>
</head>
<body>
  <section class="banner banner--tall">
    <div class="map-area" role="img" aria-label="Road map of the Iberian Peninsula with Portugal outlined"></div>
    <svg class="cursor" viewBox="0 0 56 92" aria-hidden="true">
      <path d="M2 2 L54 54 L32 54 L42 88 L32 90 L22 58 L2 74 Z" fill="var(--cursor)" stroke="#000" stroke-width="2"/>
    </svg>
    <div class="headline-box"><span>Over</span><span>2000</span></div>
    <p class="subline">New<br>Portugal<br>Listings</p>
    <div class="cta">Click Here</div>
  </section>

  <section class="banner banner--wide">
    <div class="map-area" role="img" aria-label="Road map of Portugal with Lisbon marked"></div>
    <svg class="cursor" viewBox="0 0 56 92" aria-hidden="true">
      <path d="M2 2 L54 54 L32 54 L42 88 L32 90 L22 58 L2 74 Z" fill="var(--cursor)" stroke="#000" stroke-width="3"/>
    </svg>
    <div class="headline-box">Over 2000</div>
    <p class="subline">New Portugal Listings</p>
  </section>
</body>
</html>
```